nestliva - Ballon Design

I need a Ballon designed. Please use the psb file ballon_template.psb as template.

I would like to have a ballon designed similar to the file "example.png".
instead of the pellu tot logo please use my attached logo "nestliva logo.ai"

The text should be the same " IT'S A MOM" but the logo should be different.

I should look like more elegant. should be also white background. But for the design feel free.

thanks.

Please also add the webpage "www.nestliva.eu" on the ballon design.

```html
<!DOCTYPE html>
<html lang="en">
<head>
<meta charset="utf-8">
<title>nestliva – It's a mom balloon</title>
<link rel="stylesheet" href="https://fonts.googleapis.com/css2?family=Courgette&family=Josefin+Sans:wght@400&display=swap">
<style>
  :root {
    --paper: #ffffff;
    --outline: #5a5a5a;
    --gold: #c9a24a;
    --gold-light: #f1dc9a;
    --blue: #4a69a3;
    --pink: #cf819f;
  }
  html, body {
    margin: 0;
    padding: 0;
    width: 935px;
    height: 1200px;
    overflow: hidden;
    background: var(--paper);
  }
  .balloon {
    display: block;
    width: 935px;
    height: 1200px;
  }
  .balloon-outline { fill: var(--paper); stroke: var(--outline); stroke-width: 4; }
  .ring-outer { fill: none; stroke: url(#goldStroke); stroke-width: 4; }
  .ring-inner { fill: none; stroke: url(#goldStroke); stroke-width: 4; stroke-dasharray: 700 60; }
  .ring-dot { fill: var(--paper); stroke: var(--gold); stroke-width: 4; }
  .web-address {
    font-family: "Josefin Sans", sans-serif;
    font-size: 44px;
    letter-spacing: 9px;
    fill: var(--gold);
  }
  .headline {
    font-family: "Courgette", cursive;
    text-anchor: middle;
  }
  .headline-its, .headline-a { fill: var(--blue); }
  .headline-mom { fill: var(--pink); }
  .brand-name {
    font-family: "Courgette", cursive;
    font-size: 104px;
    text-anchor: middle;
    fill: var(--blue);
  }
</style>
</head>
<body>
<svg class="balloon" viewBox="0 0 1275 1636" preserveAspectRatio="xMidYMid meet" xmlns="http://www.w3.org/2000/svg">
  <defs>
    <linearGradient id="goldStroke" x1="0" y1="0" x2="1" y2="1">
      <stop offset="0" stop-color="#c9a24a"/>
      <stop offset="0.5" stop-color="#f3e2a4"/>
      <stop offset="1" stop-color="#c49a3e"/>
    </linearGradient>
    <linearGradient id="leafTone" x1="0" y1="0" x2="1" y2="1">
      <stop offset="0" stop-color="#e7cf86" stop-opacity="0.55"/>
      <stop offset="1" stop-color="#f6ebc5" stop-opacity="0.35"/>
    </linearGradient>
    <path id="addressArc" d="M 250 235 A 560 560 0 0 1 1150 400"/>
  </defs>

  <path class="balloon-outline"
    d="M 560 1268 A 625 625 0 1 1 715 1268
       C 710 1350 728 1470 705 1535
       C 692 1570 668 1585 664 1605
       C 656 1640 598 1640 592 1605
       C 588 1585 562 1568 555 1535
       C 545 1470 566 1350 560 1268 Z"/>
  <circle class="balloon-outline" cx="628" cy="1622" r="8"/>

  <circle class="ring-outer" cx="640" cy="645" r="565"/>
  <circle class="ring-inner" cx="640" cy="645" r="525"/>
  <circle class="ring-dot" cx="428" cy="155" r="8"/>
  <circle class="ring-dot" cx="1140" cy="450" r="8"/>
  <circle class="ring-dot" cx="875" cy="1105" r="8"/>

  <text class="web-address"><textPath href="#addressArc">www.nestliva.eu</textPath></text>

  <path role="img" aria-label="Golden leafy branch ornament curving along the lower left of the ring"
    fill="url(#leafTone)"
    d="M 20 600 C 90 620 150 720 170 780 C 230 850 320 900 340 940
       C 300 1000 300 1060 270 1080 C 200 1040 150 990 130 930
       C 80 860 40 760 20 600 Z"/>

  <text class="headline headline-its" x="660" y="500" font-size="265">It’s</text>
  <text class="headline headline-a" x="655" y="690" font-size="300">a</text>
  <text class="headline headline-mom" x="672" y="885" font-size="320">mom</text>

  <text class="brand-name" x="640" y="1075">nestliva</text>
</svg>
</body>
</html>
```